Recruitment of Brackwell Staffing for the UK market

I want a website for the UK market to attract businesses and companies to come to us for Philipine labour. We want an information site that gives all information on what we do and how we can recruit Philippine labour.
This is a recruitment site for companies to contact us with their requirements for skilled workers coming from the Philipines over to the UK to work.

Target Market(s)

Uk Companies and businesses who want Philipine skilled workers

Industry/Entity Type

REcruitment

Coding

Coded - Design and coding required

Number of Pages Required

5+ page

Font styles to use
Sans Serif

Colors
0054AA
0677BA
7BADD7
CADEEF
E8F1F8
0094D4
00A9DD
6FCCEA
C7EBF8
E9F6FB
EE7325
F08F49
F5BC92
FAE3D3
FDF4ED
EB3D1F
EC4F4E
F09395
F8D3D4
FCEDEE

Requirements
Must have
• Look professional and corperate with drop down menus for Home ,about, services,articles. training , contact us
Nice to have
• Look at Tolvery recruitment- https://tolveryrecruitment.example.co.uk/. This is my current site - https://www.brackwellstaffing.example.com/
Should not have
• Cartoons or silly pictures , needs to be corperate looking

```html
<!DOCTYPE html>
<html lang="en">
<head>
<meta charset="utf-8">
<title>Brackwell Staffing – Skilled Workers from the Philippines</title>
<link href="https://fonts.googleapis.com/css2?family=Inter:wght@400;500;600;700&display=swap" rel="stylesheet">
<style>
:root{
  --red:#9a3434;
  --ink:#1c1c1c;
  --body:#555;
  --cream:#f9f6f1;
  --white:#fff;
  --dark:#2b2b2b;
  --line:#8a8a8a;
  --mapblue:#9db8e8;
}
*{margin:0;padding:0;box-sizing:border-box}
html,body{width:1200px;height:4693px;overflow:hidden}
body{font-family:'Inter',sans-serif;color:var(--ink);background:var(--cream);position:relative}
.abs{position:absolute}
a{color:inherit;text-decoration:none}
.photo{position:absolute}
.btn{position:absolute;display:flex;align-items:center;justify-content:center;border-radius:26px;font-size:15px}
.btn-red{background:var(--red);color:var(--white)}
.btn-outline{border:1.5px solid var(--red);color:var(--red);background:transparent}
.btn-white{background:var(--white);color:var(--red)}
.h2{font-size:33px;font-weight:400;letter-spacing:.3px;text-transform:uppercase}
.txt{font-size:12.5px;line-height:23.5px;color:var(--body)}

/* header */
.site-header{position:absolute;top:0;left:0;width:1200px;height:575px;background:var(--white)}
.brand{position:absolute;left:100px;top:33px;display:flex;align-items:center;gap:10px;font-size:24px;font-weight:700;color:var(--red)}
.brand-dot{width:16px;height:16px;background:var(--red);border-radius:50%}
.nav{position:absolute;top:41px;font-size:14px;color:var(--ink)}
.hero-title{left:102px;top:218px;font-size:50px;line-height:58px;font-weight:700;text-transform:uppercase}
.hero-sub{left:102px;top:408px;font-size:12.5px}
.hero-photo{left:614px;top:109px;width:471px;height:466px;border-top-left-radius:120px;background:linear-gradient(160deg,#c9cfd6,#5d6a78 55%,#8a6a50)}

/* about */
.about-photo{left:0;top:670px;width:422px;height:543px;background:linear-gradient(170deg,#d7d2cb,#6f7567 60%,#514d45)}
.about-photo-small{left:976px;top:974px;width:224px;height:239px;background:linear-gradient(160deg,#c8cbc2,#5e8770 60%,#d7d2ca)}
.about-rule{left:488px;top:930px;width:510px;height:1px;background:var(--line)}

/* working */
.map{left:645px;top:1232px;width:370px;height:420px;background:linear-gradient(180deg,#e6edf8,var(--mapblue) 55%,#d9e3f4)}

/* help */
.help-photo{left:206px;top:1705px;width:393px;height:422px;background:linear-gradient(160deg,#d6d1c7,#a78f6c 50%,#d9742f)}
.help-photo-small{left:93px;top:1819px;width:195px;height:259px;background:linear-gradient(160deg,#c79a6d,#e5c53a 50%,#7b5a3a);border:3px solid var(--white)}

/* cards */
.card-divider{position:absolute;top:2225px;width:1px;height:388px;background:var(--line)}
.card-title{font-size:16px;font-weight:500;text-transform:uppercase}
.read-more{font-size:14px;font-weight:500;color:var(--red)}

/* start band */
.start-band{left:0;top:2708px;width:1200px;height:433px;background:linear-gradient(180deg,#485862,#3a3d3b 55%,#55503f)}
.start-title{top:2838px;width:1200px;text-align:center;color:var(--white);font-size:33px;text-transform:uppercase}
.start-text{left:225px;top:2896px;width:750px;text-align:center;color:var(--white);font-size:12.5px;line-height:23.5px;font-weight:700}

/* articles */
.article-img{position:absolute;top:3314px;width:261px;height:306px}
.article-date{font-size:12.5px;color:var(--body)}
.article-title{font-size:17px;font-weight:600}

/* contact */
.field{position:absolute;font-size:13px;color:var(--body);display:flex;align-items:center;gap:10px}
.field-line{position:absolute;height:1px;background:#777}

/* footer */
.site-footer{left:0;top:4438px;width:1200px;height:255px;background:var(--dark);color:#ddd}
.foot-link{position:absolute;left:550px;font-size:13px;color:#ccc}
</style>
</head>
<body>

<header class="site-header">
  <a class="brand" href="#"><span class="brand-dot"></span>Brackwell Staffing</a>
  <a class="nav" style="left:545px" href="#">Home</a>
  <a class="nav" style="left:618px" href="#">About</a>
  <a class="nav" style="left:692px" href="#">Services</a>
  <a class="nav" style="left:783px" href="#">Articles</a>
  <a class="nav" style="left:867px" href="#">Training</a>
  <a class="btn btn-outline" style="left:952px;top:25px;width:135px;height:50px" href="#">Contact Us</a>

  <h1 class="abs hero-title">Hiring skilled<br>workers from<br>the Philippines</h1>
  <p class="abs hero-sub">Expand Your Workforce with Top Talent from the Philippines</p>
  <a class="btn btn-red" style="left:102px;top:461px;width:120px;height:46px" href="#">Hire Now</a>

  <div class="photo hero-photo" role="img" aria-label="Smiling skilled worker in a denim shirt at a workbench"></div>
</header>

<section class="about">
  <div class="photo about-photo" role="img" aria-label="Smiling young woman in a work apron with arms crossed"></div>
  <h2 class="abs h2" style="left:488px;top:724px">What the business is about</h2>
  <p class="abs txt" style="left:488px;top:793px;width:512px;font-size:11.5px">We source skilled workers directly from the Philippines to work in the UK. With offices , training locations and specialist recruiters we can find the highest quality individuals to add value and resources to any UK buisness. We delivery quality based on vast experience over a number of years.</p>
  <div class="abs about-rule"></div>
  <h3 class="abs" style="left:488px;top:968px;font-size:20px;font-weight:400">What we do</h3>
  <p class="abs txt" style="left:488px;top:1002px;width:420px;font-size:11.5px">Our company has been estabilished in the Philippines for over 20 years. We have mainly been recruiting philippine workers for the off shore industry in asia but since brexit and the new rules on skilled workers entering the UK we have been working with UK companies who now have chance to recruit some of the finest hard working talent from the Philippines for their companies..</p>
  <div class="photo about-photo-small" role="img" aria-label="Craftsman in an apron working at a pottery workshop"></div>
</section>

<section class="working">
  <h2 class="abs h2" style="left:228px;top:1372px;width:300px;text-align:right;line-height:42px">Working<br>together</h2>
  <p class="abs txt" style="left:228px;top:1468px;width:300px;text-align:right">We recruit the finest talent available with our dedicated 200 strong team. Our centres are highlighted in red dots on the map.</p>
  <div class="abs map" role="img" aria-label="Map of the Philippines marking recruitment centres in Baguio, Manila, Batangas, Bacolod and Davao"></div>
</section>

<section class="help">
  <div class="photo help-photo" role="img" aria-label="Smiling construction worker in a hard hat and safety vest"></div>
  <div class="photo help-photo-small" role="img" aria-label="Worker holding a yellow hard hat with a tool belt"></div>
  <h2 class="abs h2" style="left:677px;top:1766px">How we help</h2>
  <p class="abs txt" style="left:677px;top:1826px;width:290px">We work with companies to find skilled workers that meet the UK requirements for Visas and work permits. We guide you through the whole process and deliver highly trained people that add value to your business. We are here to help both the companies and the Philippino people to gain a better standard of living for their families.</p>
  <a class="btn btn-red" style="left:674px;top:2040px;width:120px;height:47px" href="#">Hire Now</a>
</section>

<section class="services">
  <div class="card-divider" style="left:430px"></div>
  <div class="card-divider" style="left:727px"></div>

  <svg class="abs" style="left:160px;top:2262px" width="62" height="72" viewBox="0 0 62 72" fill="none" stroke="#9a3434" stroke-width="2" aria-hidden="true">
    <path d="M4 2h38l16 16v52H4z"/><path d="M42 2v16h16"/>
    <rect x="10" y="24" width="8" height="8"/><path d="M12 28l2 2 4-4"/><line x1="24" y1="28" x2="50" y2="28"/>
    <rect x="10" y="40" width="8" height="8"/><path d="M12 44l2 2 4-4"/><line x1="24" y1="44" x2="50" y2="44"/>
    <rect x="10" y="56" width="8" height="8"/><line x1="24" y1="60" x2="50" y2="60"/>
  </svg>
  <h3 class="abs card-title" style="left:160px;top:2354px">UK skilled workers list</h3>
  <p class="abs txt" style="left:160px;top:2393px;width:240px">The UK government since brexit have developed a new system based on points (similar to Australia) when recruiting from outside of the UK. Previuosly EU citizens could work in...</p>
  <a class="abs read-more" style="left:160px;top:2562px" href="#">Read More ↗</a>

  <svg class="abs" style="left:455px;top:2262px" width="70" height="72" viewBox="0 0 70 72" fill="none" stroke="#9a3434" stroke-width="2" aria-hidden="true">
    <path d="M10 2h56v52H34"/><path d="M10 2a6 6 0 0 0-6 6v40h16"/>
    <line x1="22" y1="14" x2="56" y2="14"/><line x1="22" y1="24" x2="56" y2="24"/><line x1="38" y1="34" x2="56" y2="34"/>
    <circle cx="20" cy="46" r="9"/><path d="M14 54v16l6-4 6 4V54"/>
  </svg>
  <h3 class="abs card-title" style="left:455px;top:2354px">Sponsor licence</h3>
  <p class="abs txt" style="left:455px;top:2393px;width:250px">If you have areas of your business that meet the entry requirements of skilled labour your next step is to gain a sponsor licence for your business. There are different types of licences depending on the size of the busines...</p>
  <a class="abs read-more" style="left:455px;top:2562px" href="#">Read More ↗</a>

  <svg class="abs" style="left:752px;top:2262px" width="86" height="72" viewBox="0 0 86 72" fill="none" stroke="#9a3434" stroke-width="2" aria-hidden="true">
    <rect x="6" y="2" width="74" height="46" rx="3"/><rect x="14" y="10" width="20" height="14"/>
    <line x1="40" y1="12" x2="70" y2="12"/><line x1="40" y1="20" x2="70" y2="20"/><line x1="14" y1="34" x2="70" y2="34"/>
    <path d="M36 48l7 8 7-8"/><line x1="6" y1="64" x2="80" y2="64"/>
    <circle cx="8" cy="64" r="4"/><circle cx="43" cy="64" r="4"/><circle cx="78" cy="64" r="4"/>
  </svg>
  <h3 class="abs card-title" style="left:752px;top:2354px">Recruitment timeline</h3>
  <p class="abs txt" style="left:752px;top:2393px;width:250px">Brief us on the job profiles – this is passed on to our teams in the Philippines.</p>
  <p class="abs txt" style="left:760px;top:2464px;width:240px">• &nbsp;- Our teams in the Philippines<br>&nbsp;&nbsp;&nbsp;source suitable candidates,<br>&nbsp;&nbsp;&nbsp;documentation required for each...</p>
  <a class="abs read-more" style="left:752px;top:2562px" href="#">Read More ↗</a>
</section>

<section class="start">
  <div class="abs start-band" role="img" aria-label="Mountain landscape with a winding road at dusk"></div>
  <h2 class="abs start-title">Where to start</h2>
  <p class="abs start-text">We need to know what your issues are and how we can understand the personnal you require , over what time frame and the number of employees you need. Once this is estabilished we start sourcing workers in the Philippines that meet your criteria while starting the process in the UK to be able to have all the documents in place to deliver your company hard working skilled individuals.</p>
  <a class="btn btn-white" style="left:539px;top:3006px;width:118px;height:47px" href="#">Hire Now</a>
</section>

<section class="articles">
  <h2 class="abs h2" style="left:168px;top:3234px">Latest articles</h2>
  <a class="abs" style="left:960px;top:3246px;font-size:14px;font-weight:500;color:var(--red);border-bottom:1.5px solid var(--red);padding-bottom:4px" href="#">VIEW ALL</a>

  <div class="article-img" style="left:169px;background:linear-gradient(160deg,#9fb27a,#8a4a3a 55%,#d8c8a8)" role="img" aria-label="Woman in a plaid shirt measuring timber on a workbench"></div>
  <div class="article-img" style="left:468px;background:linear-gradient(160deg,#d6d8da,#7a8b96 55%,#c9b48a)" role="img" aria-label="Technician repairing a bicycle wheel in a workshop"></div>
  <div class="article-img" style="left:768px;background:linear-gradient(160deg,#cfe0ef,#7e9ab8 50%,#e07a2e)" role="img" aria-label="Two engineers in hard hats reviewing a tablet near tower blocks"></div>

  <div class="abs" style="left:174px;top:3641px;width:255px">
    <p class="article-date">26 mar 2023</p>
    <h3 class="article-title" style="margin-top:10px">Urna id consectetur</h3>
    <p class="txt" style="margin-top:6px">Lorem ipsum dolor sit amet consectetur. Quis arcu lectus amet ultrices egestas consequat mi. Urna id consectetur ultricies dui aliquet etiam neque sapien...</p>
    <a class="read-more" style="display:block;margin-top:14px" href="#">Read More ↗</a>
  </div>
  <div class="abs" style="left:469px;top:3641px;width:255px">
    <p class="article-date">26 mar 2023</p>
    <h3 class="article-title" style="margin-top:10px">Urna id consectetur</h3>
    <p class="txt" style="margin-top:6px">Lorem ipsum dolor sit amet consectetur. Quis arcu lectus amet ultrices egestas consequat mi. Urna id consectetur ultricies dui aliquet etiam neque sapien...</p>
    <a class="read-more" style="display:block;margin-top:14px" href="#">Read More ↗</a>
  </div>
  <div class="abs" style="left:769px;top:3641px;width:255px">
    <p class="article-date">26 mar 2023</p>
    <h3 class="article-title" style="margin-top:10px">Urna id consectetur</h3>
    <p class="txt" style="margin-top:6px">Lorem ipsum dolor sit amet consectetur. Quis arcu lectus amet ultrices egestas consequat mi. Urna id consectetur ultricies dui aliquet etiam neque sapien...</p>
    <a class="read-more" style="display:block;margin-top:14px" href="#">Read More ↗</a>
  </div>
</section>

<section class="contact">
  <h2 class="abs h2" style="top:3982px;width:1200px;text-align:center">Contact us today</h2>
  <div class="field" style="left:204px;top:4077px">
    <svg width="14" height="14" viewBox="0 0 14 14" fill="none" stroke="#555" stroke-width="1.3"><circle cx="7" cy="4.5" r="3"/><path d="M1.5 13c.5-3 3-4.5 5.5-4.5s5 1.5 5.5 4.5"/></svg>Full Name</div>
  <div class="field-line" style="left:204px;top:4108px;width:357px"></div>
  <div class="field" style="left:592px;top:4077px">
    <svg width="14" height="14" viewBox="0 0 14 14" fill="none" stroke="#555" stroke-width="1.3"><path d="M3 1.5l2.5 3-1.5 1.5c.8 1.8 2.2 3.2 4 4l1.5-1.5 3 2.5-1.5 2C6 12.5 1.5 8 1 3z"/></svg>Phone Number</div>
  <div class="field-line" style="left:592px;top:4108px;width:357px"></div>
  <div class="field" style="left:204px;top:4135px">
    <svg width="14" height="14" viewBox="0 0 14 14" fill="none" stroke="#555" stroke-width="1.3"><rect x="1" y="3" width="12" height="9"/><path d="M1 3l6 5 6-5"/></svg>Email Address</div>
  <div class="field-line" style="left:204px;top:4164px;width:745px"></div>
  <div class="field" style="left:204px;top:4194px">
    <svg width="14" height="14" viewBox="0 0 14 14" fill="none" stroke="#555" stroke-width="1.3"><path d="M12 8v5H1V2h5"/><path d="M10.5 1.5l2 2L7 9H5V7z"/></svg>Your message here</div>
  <div class="field-line" style="left:204px;top:4290px;width:745px"></div>
  <a class="btn btn-outline" style="left:539px;top:4317px;width:118px;height:48px;font-size:14px" href="#">SEND US</a>
</section>

<footer class="abs site-footer">
  <a class="brand" style="left:118px;top:58px" href="#"><span class="brand-dot"></span>Brackwell Staffing</a>
  <p class="abs" style="left:112px;top:114px;font-size:11.5px;color:#ccc;line-height:20px">t. &nbsp;&nbsp;(020) 555-0148<br>e. &nbsp;&nbsp;hello@brackwellstaffing.example.com<br>l. &nbsp;&nbsp;&nbsp;14 Halden Row, Marlow Vale, MV4 2QT</p>

  <a class="foot-link" style="top:40px" href="#">Home</a>
  <a class="foot-link" style="top:67px" href="#">About</a>
  <a class="foot-link" style="top:94px" href="#">Services</a>
  <a class="foot-link" style="top:121px" href="#">Articles</a>
  <a class="foot-link" style="top:148px" href="#">Training</a>

  <p class="abs" style="left:681px;top:48px;font-size:11.5px;font-weight:600;color:#ddd">Receive latest news &amp;report from the Brackwell Staffing</p>
  <div class="abs" style="left:681px;top:84px;width:341px;height:34px;border:1px solid #aaa;border-radius:17px;display:flex;align-items:center;font-size:10px;color:#aaa">
    <span style="flex:1;padding-left:20px">Your email</span>
    <span style="border-left:1px solid #aaa;height:100%;display:flex;align-items:center;padding:0 16px;color:#fff;font-size:11px">SUBSCRIBE</span>
  </div>

  <div class="abs" style="left:112px;top:198px;width:904px;height:1px;background:#666"></div>
  <p class="abs" style="left:112px;top:219px;font-size:11px;color:#bbb">© 2023 All Rights Reserved | Brackwell Staffing Ltd</p>
  <div class="abs" style="left:946px;top:219px;display:flex;gap:10px">
    <span style="width:14px;height:14px;border:1.3px solid #aaa;border-radius:50%"></span>
    <span style="width:14px;height:14px;border:1.3px solid #aaa;border-radius:50%"></span>
    <span style="width:14px;height:14px;border:1.3px solid #aaa;border-radius:50%"></span>
  </div>
</footer>

</body>
</html>
```